Price Calculator as Responsive Web App to support Sales People

We need to build a simple micro web app to support sales people in making quotes. We already have a backend that can take a number of parameters and create a quote. We need put a responsive web app on top of this so that our people on the road can easily do their price simulations.

We need two pages. One for the input and another for the results. No menus, navigations, etc. It is 6 different inputs as shown with boxes in the sketch. They don't need to be boxed, but some of them have a bit of instruction text that clearly need to belong to the input.

This needs to be responsive, but first and foremost designed for smartphones. I have included a background gradient that we would like to use -- or a variant of it. We expect this to be delivered as HTML/CSS + images so that we can quickly write a few pieces of JavaScript ourselves to wire it up to our price simulator.

Industry/Entity Type

Information Technology

Coding

Coded - Design and coding required

Number of Pages Required

2 page

Font styles to use
Sans Serif

Requirements
Must have
• Responsive design
• Easy to wire up JavaScript to the HTML/CSS
Nice to have
• Some quick way to pick number of months. +/- buttons to add remove a year or 3 months. Same thing with number of items. Add 10 or 5 quickly.
• Maybe some parallax effect while scrolling as long as it is not distracting.
Should not have
• Toolbars, Menus, Navigations, Banners, etc. This is just a single micro app.

```html
<!DOCTYPE html>
<html lang="en">
<head>
<meta charset="utf-8">
<title>Price Calculator – Results</title>
<link href="https://fonts.googleapis.com/css2?family=Nunito:wght@400;600&display=swap" rel="stylesheet">
<style>
  :root {
    --bg-top: #041a2e;
    --bg-bottom: #053a64;
    --head-row: #0a1e34;
    --row-light: #06476f;
    --row-dark: #052b4d;
    --total-row: #2198da;
    --cap-row: #ffb400;
    --grid-line: rgba(150, 190, 220, 0.45);
    --text: #ffffff;
    --axis: #ffffff;
    --bar-blue-start: #5ccbf0;
    --bar-blue-end: #2393d6;
    --bar-orange-start: #ffb600;
    --bar-orange-end: #ff8200;
  }
  * { margin: 0; padding: 0; box-sizing: border-box; }
  html, body {
    width: 1092px;
    height: 1200px;
    overflow: hidden;
  }
  body {
    position: relative;
    background: linear-gradient(180deg, var(--bg-top) 0%, var(--bg-bottom) 100%);
    font-family: "Nunito", sans-serif;
    color: var(--text);
  }
  .quote-table {
    position: absolute;
    left: 101px;
    top: 58px;
    width: 903px;
    border-collapse: collapse;
    font-size: 27px;
    border: 1px solid var(--grid-line);
  }
  .quote-table th,
  .quote-table td {
    text-align: left;
    font-weight: 400;
    border-left: 1px solid var(--grid-line);
    padding: 0;
  }
  .quote-table th { font-weight: 600; height: 68px; background: var(--head-row); }
  .quote-table .col-label { width: 283px; padding-left: 71px; }
  .quote-table .col-month { width: 344px; padding-left: 136px; }
  .quote-table th.col-month { padding-left: 129px; }
  .quote-table .col-year { padding-left: 63px; }
  .row-item td { height: 90px; background: var(--row-light); }
  .row-engine td { height: 71px; background: var(--row-dark); }
  .row-storage td { height: 93px; background: var(--row-light); }
  .row-tip td { height: 74px; background: var(--row-dark); }
  .row-total td { height: 83px; background: var(--total-row); }
  .row-cap td { height: 83px; background: var(--cap-row); }
  .cost-chart {
    position: absolute;
    left: 0;
    top: 0;
    width: 1092px;
    height: 1200px;
  }
  .cost-chart text {
    font-family: "Nunito", sans-serif;
    font-size: 16px;
    fill: var(--text);
  }
</style>
</head>
<body>
  <table class="quote-table">
    <thead>
      <tr><th class="col-label"></th><th class="col-month">Per Months</th><th class="col-year">Per Year</th></tr>
    </thead>
    <tbody>
      <tr class="row-item"><td class="col-label">Item</td><td class="col-month">350</td><td class="col-year">4200</td></tr>
      <tr class="row-engine"><td class="col-label">Engine</td><td class="col-month">250</td><td class="col-year">3000</td></tr>
      <tr class="row-storage"><td class="col-label">Storage</td><td class="col-month">200</td><td class="col-year">2400</td></tr>
      <tr class="row-tip"><td class="col-label">Tip</td><td class="col-month">52</td><td class="col-year">630</td></tr>
      <tr class="row-total"><td class="col-label">Total</td><td class="col-month">852</td><td class="col-year">10230</td></tr>
      <tr class="row-cap"><td class="col-label">Cap</td><td class="col-month">1278</td><td class="col-year">15345</td></tr>
    </tbody>
  </table>

  <svg class="cost-chart" viewBox="0 0 1092 1200" role="img" aria-label="Bar chart comparing cost totals against the cap">
    <defs>
      <linearGradient id="bar-blue" x1="0" x2="1" y1="0" y2="0">
        <stop offset="0" stop-color="var(--bar-blue-start)"/>
        <stop offset="1" stop-color="var(--bar-blue-end)"/>
      </linearGradient>
      <linearGradient id="bar-orange" x1="0" x2="1" y1="0" y2="0">
        <stop offset="0" stop-color="var(--bar-orange-start)"/>
        <stop offset="1" stop-color="var(--bar-orange-end)"/>
      </linearGradient>
    </defs>

    <g class="bars">
      <rect x="233" y="726" width="712" height="83" fill="url(#bar-orange)"/>
      <rect x="233" y="809" width="538" height="84" fill="url(#bar-blue)"/>
      <rect x="233" y="893" width="388" height="84" fill="url(#bar-blue)"/>
      <rect x="233" y="977" width="538" height="81" fill="url(#bar-blue)"/>
      <line x1="233" y1="893" x2="771" y2="893" stroke="#0a3558" stroke-width="1.5"/>
      <line x1="233" y1="977" x2="771" y2="977" stroke="#0a3558" stroke-width="1.5"/>
      <line x1="806" y1="893" x2="939" y2="893" stroke="#3a6f96" stroke-width="1" stroke-dasharray="5 4"/>
    </g>

    <g class="axes" stroke="var(--axis)" stroke-width="2">
      <line x1="215" y1="687" x2="215" y2="1087"/>
      <line x1="214" y1="1086" x2="967" y2="1086"/>
      <line x1="205" y1="728" x2="215" y2="728"/>
      <line x1="205" y1="809" x2="215" y2="809"/>
      <line x1="205" y1="893" x2="215" y2="893"/>
      <line x1="205" y1="978" x2="215" y2="978"/>
      <line x1="205" y1="1056" x2="215" y2="1056"/>
      <line x1="259" y1="1079" x2="259" y2="1096"/>
      <line x1="341" y1="1079" x2="341" y2="1096"/>
      <line x1="426" y1="1079" x2="426" y2="1096"/>
      <line x1="510" y1="1079" x2="510" y2="1096"/>
      <line x1="590" y1="1079" x2="590" y2="1096"/>
      <line x1="664" y1="1079" x2="664" y2="1096"/>
      <line x1="746" y1="1079" x2="746" y2="1096"/>
      <line x1="831" y1="1079" x2="831" y2="1096"/>
      <line x1="915" y1="1079" x2="915" y2="1096"/>
    </g>

    <g class="y-labels" text-anchor="end">
      <text x="194" y="734">05</text>
      <text x="194" y="815">04</text>
      <text x="194" y="899">03</text>
      <text x="194" y="984">02</text>
      <text x="194" y="1062">01</text>
    </g>
    <g class="x-labels" text-anchor="middle">
      <text x="259" y="1123">01</text>
      <text x="341" y="1123">02</text>
      <text x="426" y="1123">03</text>
      <text x="510" y="1123">04</text>
      <text x="590" y="1123">05</text>
      <text x="664" y="1123">06</text>
      <text x="746" y="1123">07</text>
      <text x="831" y="1123">08</text>
      <text x="915" y="1123">09</text>
    </g>
  </svg>
</body>
</html>
```